TORVEL Industrial Maintenance

I offer repair and maintenance services of industrial mechanics in Quebec. I would like a creation that reflects confidence, competence, professionalism and dynamism. I like the orange color and the blue color.

Target Market(s)

Industries and Manufacturing companies using industrial machinery for the manufacture of their products.

Industry/Entity Type

Manufacturing

Contact Information for Business Card

TORVEL Maintenance Industrielle
Tél: (450)-318-5947
Courriel: torvel.mnt@boitemel-exemple.com

Font styles to use
Sans Serif

Colors
f78f20
0455a3

Requirements
Must have
• My company name: TORVEL Maintenance Industrielle My phone: (450) -318-5947 My email: torvel.mnt@boitemel-exemple.com
Nice to have
• Integrate a representative logo of the mechanics (gears, mechanical parts)

```html
<!DOCTYPE html>
<html lang="fr">
<head>
<meta charset="utf-8">
<title>TORVEL Maintenance Industrielle – Carte professionnelle</title>
<link href="https://fonts.googleapis.com/css2?family=Open+Sans:wght@400;600;700&display=swap" rel="stylesheet">
<style>
  :root {
    --page-bg: #e9e6e2;
    --card-bg: #ffffff;
    --brand-blue: #1f5aa6;
    --tab-blue: #2f7bc8;
    --text-grey: #777777;
    --divider: #d8d8d8;
  }
  * { margin: 0; padding: 0; box-sizing: border-box; }
  html, body {
    width: 1200px; height: 1000px; overflow: hidden;
    background: var(--page-bg);
    font-family: "Open Sans", Arial, sans-serif;
  }
  .business-card {
    position: absolute;
    left: 266px;
    width: 666px; height: 397px;
    background: var(--card-bg);
    border-radius: 24px;
    box-shadow: 0 4px 14px rgba(0,0,0,0.18);
  }
  .business-card--front { top: 74px; }
  .business-card--back  { top: 533px; }

  .edge-tab {
    position: absolute; top: 119px;
    width: 12px; height: 160px;
    background: var(--tab-blue);
  }
  .edge-tab--left  { left: 0; border-radius: 0 6px 6px 0; }
  .edge-tab--right { right: 0; border-radius: 6px 0 0 6px; }

  .brand-mark {
    position: absolute; left: 54px; top: 150px;
    width: 290px;
    display: flex; align-items: center; gap: 14px;
    color: var(--brand-blue);
    font-weight: 700;
  }
  .brand-mark__dot {
    flex: none;
    width: 54px; height: 54px; border-radius: 50%;
    background: var(--brand-blue);
  }
  .brand-mark__name { font-size: 50px; line-height: 1; letter-spacing: 1px; }
  .brand-mark__tagline { font-size: 12.5px; letter-spacing: 0.6px; text-transform: uppercase; margin-top: 6px; }

  .divider {
    position: absolute; left: 374px; top: 136px;
    width: 1px; height: 136px;
    background: var(--divider);
  }

  .contact-block {
    position: absolute; left: 398px; top: 132px;
  }
  .contact-block__name {
    font-size: 22px; font-weight: 600; color: var(--brand-blue); line-height: 30px;
  }
  .contact-block__role {
    font-size: 16px; color: var(--text-grey); line-height: 22px;
  }
  .contact-block__lines { margin-top: 26px; }
  .contact-line {
    display: flex; align-items: center; gap: 6px;
    font-size: 16px; color: var(--text-grey); line-height: 26px;
  }
  .contact-line svg { width: 14px; height: 14px; fill: var(--brand-blue); flex: none; }
</style>
</head>
<body>

<section class="business-card business-card--front">
  <span class="edge-tab edge-tab--left"></span>
  <span class="edge-tab edge-tab--right"></span>
  <div class="brand-mark">
    <span class="brand-mark__dot"></span>
    <div>
      <div class="brand-mark__name">TORVEL</div>
      <div class="brand-mark__tagline">Maintenance Industrielle</div>
    </div>
  </div>
  <span class="divider"></span>
  <div class="contact-block">
    <div class="contact-block__name">Martin Dufresne</div>
    <div class="contact-block__role">CEO / Owner</div>
    <div class="contact-block__lines">
      <div class="contact-line">
        <svg viewBox="0 0 16 16"><path d="M2 6c0-2 2-3 6-3s6 1 6 3v1h-3V5.5H5V7H2zM4 8h8l2 5H2z"/></svg>
        (450) -318-5947
      </div>
      <div class="contact-line">
        <svg viewBox="0 0 16 16"><path d="M1 3h14v10H1zM2.5 4.5v.4L8 9l5.5-4.1v-.4zM2.5 6.7v4.8h11V6.7L8 10.8z"/></svg>
        torvel.mnt@boitemel-exemple.com
      </div>
    </div>
  </div>
</section>

<section class="business-card business-card--back">
  <span class="edge-tab edge-tab--left"></span>
  <span class="edge-tab edge-tab--right"></span>
  <div class="brand-mark">
    <span class="brand-mark__dot"></span>
    <div>
      <div class="brand-mark__name">TORVEL</div>
      <div class="brand-mark__tagline">Maintenance Industrielle</div>
    </div>
  </div>
  <span class="divider"></span>
  <div class="contact-block">
    <div class="contact-block__name">Martin Dufresne</div>
    <div class="contact-block__role">CEO / Owner</div>
    <div class="contact-block__lines">
      <div class="contact-line">
        <svg viewBox="0 0 16 16"><path d="M2 6c0-2 2-3 6-3s6 1 6 3v1h-3V5.5H5V7H2zM4 8h8l2 5H2z"/></svg>
        (450) -318-5947
      </div>
      <div class="contact-line">
        <svg viewBox="0 0 16 16"><path d="M1 3h14v10H1zM2.5 4.5v.4L8 9l5.5-4.1v-.4zM2.5 6.7v4.8h11V6.7L8 10.8z"/></svg>
        torvel.mnt@boitemel-exemple.com
      </div>
    </div>
  </div>
</section>

</body>
</html>
```